TARNVOX Profile

We need to redesign our company Profile
( Word file Attachment with all our company Information’s ) .
Pls follow the below Notes ones you start this Project:
1- Use our current Information’s the file Attachment.
2- You have the full right to change , Add and Remove any
word
3- Use Many Pictures and Drawing that match the page you
are working on .
4- Do not follow the same Profile 100% , as we are looking
for something new and Looks nice .
5- You can visit our website : www.tarnvox.example to get more
information’s
6- You can Take More Ideas , Text from our Competitors
website , Like Chatrelo.example And www.Pellicor.example or
www.dralmune.example
Updates
Dear . All Proff. Designers
We will be proud of you and your desing if you show us
your Nice work marked with this project .
Have a nice day to all
Industry/Entity Type
It Company
Look and feel
Each slider illustrates characteristics of the customer's brand and the style your logo design should communicate.

```html
<!DOCTYPE html>
<html lang="en">
<head>
<meta charset="UTF-8">
<title>TARNVOX Profile – About VoIP Service</title>
<link href="https://fonts.googleapis.com/css2?family=Arimo:wght@400;700&family=Oswald:wght@400;500&display=swap" rel="stylesheet">
<style>
  :root {
    --brand-green: #8dbb1c;
    --brand-green-dark: #7aa514;
    --text-grey: #6b6b6b;
    --title-grey: #8a8a8a;
    --rule-grey: #c9c9c9;
    --paper: #ffffff;
  }
  * { margin: 0; padding: 0; box-sizing: border-box; }
  html, body { width: 1200px; height: 900px; overflow: hidden; background: var(--paper); }
  .page {
    position: relative;
    width: 1200px;
    height: 900px;
    background: var(--paper);
    font-family: "Arimo", Arial, sans-serif;
    color: var(--text-grey);
    overflow: hidden;
  }

  /* Header */
  .header-band {
    position: absolute; left: 0; top: 0;
    width: 630px; height: 105px;
    background: linear-gradient(90deg, var(--brand-green-dark), var(--brand-green) 40%, var(--brand-green));
  }
  .brand {
    position: absolute; display: flex; align-items: center;
    font-family: "Arimo", Arial, sans-serif; font-weight: 700;
    letter-spacing: 3px; white-space: nowrap;
  }
  .brand-header { left: 60px; top: 27px; height: 66px; gap: 24px; color: var(--paper); font-size: 28px; }
  .brand-header .brand-dot { width: 66px; height: 66px; border-radius: 50%; background: var(--paper); opacity: .85; }
  .header-rule {
    position: absolute; left: 645px; top: 108px; width: 555px; height: 2px;
    background: var(--rule-grey);
  }
  .page-title {
    position: absolute; right: 42px; top: 34px;
    font-family: "Oswald", "Arial Narrow", sans-serif; font-weight: 500;
    font-size: 37px; line-height: 48px; text-transform: uppercase;
    color: var(--title-grey);
  }
  .page-title .accent { color: var(--brand-green); }

  /* Body copy */
  .intro {
    position: absolute; left: 65px; top: 140px; width: 1100px;
    font-size: 20.5px; line-height: 32px;
  }
  .intro .lead { color: var(--brand-green); font-weight: 700; }
  .features {
    position: absolute; left: 65px; top: 310px; width: 1110px;
    list-style: none; font-size: 20.5px; line-height: 37.5px;
  }
  .features li { position: relative; padding-left: 47px; }
  .features li::before {
    content: ""; position: absolute; left: 3px; top: 9px;
    width: 20px; height: 20px; border-radius: 50%;
    background: var(--brand-green);
  }

  /* Footer */
  .footer-block { position: absolute; left: 0; top: 867px; width: 33px; height: 33px; background: var(--brand-green); }
  .footer-bar { position: absolute; left: 308px; top: 867px; width: 322px; height: 33px; background: var(--brand-green); }
  .footer-rule { position: absolute; left: 630px; top: 872px; width: 450px; height: 2px; background: var(--rule-grey); }
  .brand-footer {
    left: 78px; top: 778px; width: 210px;
    flex-direction: column; align-items: center; gap: 4px;
    color: var(--title-grey); font-size: 29px; line-height: 32px;
  }
  .brand-footer .brand-dot { width: 80px; height: 80px; border-radius: 50%; background: var(--brand-green); }
  .page-number {
    position: absolute; left: 1080px; top: 853px; width: 98px; height: 33px;
    border: 2px solid var(--brand-green); background: var(--paper);
    font-family: "Oswald", "Arial Narrow", sans-serif; font-size: 20px;
    color: var(--title-grey); display: flex; align-items: center; justify-content: center;
  }
</style>
</head>
<body>
<div class="page">
  <header>
    <div class="header-band"></div>
    <div class="brand brand-header"><span class="brand-dot"></span><span>TARNVOX</span></div>
    <h1 class="page-title">About <span class="accent">VoIP Service</span></h1>
    <div class="header-rule"></div>
  </header>

  <main>
    <p class="intro">
      <span class="lead">Voice over Internet Protocol (Voice over IP, VoIP)</span> is one of a family of internet technologies. Internet tele-<br>phony refers to communications services—Voice, fax, SMS and/or voice-messaging applications—that are trans-<br>ported via the Internet, rather than the Public Switched Telephone Network (PSTN)<br>
      VoIP can facilitate tasks and provide services that may be more difficult to implement using the PSTN. Examples<br>include:
    </p>
    <ul class="features">
      <li>The ability to transmit more than one telephone call over a single broadband connection.</li>
      <li>Secure calls using standardized protocols (such as Secure Real-Time Transport Protocol).&nbsp; Most of the<br>difficulties of creating a secure telephone connection over traditional phone lines, such as digitizing and<br>digital transmission, are already in place with VoIP. It is only necessary to encrypt and authenticate the<br>existing data stream.</li>
      <li>Location independence. Only a sufficiently fast and stable Internet connection is needed to get a<br>connection from anywhere to a VoIP provider.</li>
      <li>Integration with other services available over the Internet, including video conversation, message or<br>data file exchange during the conversation, audio conferencing, managing address books, and<br>passing information about whether other people are available to interested parties.</li>
      <li>Unified Communications, the integration of VoIP with other business systems including E-mail, Customer<br>Relationship Management (CRM), and Web systems.</li>
    </ul>
  </main>

  <footer>
    <div class="footer-block"></div>
    <div class="footer-bar"></div>
    <div class="brand brand-footer"><span class="brand-dot"></span><span>TARNVOX</span></div>
    <div class="footer-rule"></div>
    <div class="page-number">PAGE: 02</div>
  </footer>
</div>
</body>
</html>
```